Brisklo Business Courses by Vantrel LLC

Need source code for this app with one lesson examples copied. The app should include the copied content from Chapter 1 of "Ledgerwork: Rates Beyond Today" which in turn consists of 4 sub-chapters.
In addition, the app must contain copy of UI and code elements such that additional sub-chapters, additional chapters, and additional lessons can be added.

Requirements
Must have
• Source code for app must target IOS. Look and feel of the app can be identical to the reference app, Brisklo.
• No reference code available.
• The content of the lessons will be replaced with non-finance related material for internal training use.
Nice to have
• Mechanism for tracking progress for single user.
• Top level code in Swift.
• Web page implementations of Chapter 1.

```html
<!DOCTYPE html>
<html lang="en">
<head>
<meta charset="utf-8">
<title>Brisklo – Rates Beyond Today</title>
<link href="https://fonts.googleapis.com/css2?family=Open+Sans:wght@300;400;600;700&display=swap" rel="stylesheet">
<style>
  :root {
    --hero-deep: #231046;
    --hero-mid: #3a2466;
    --hero-glow: #8a7fa6;
    --ink-light: #ffffff;
    --ink-soft: #e6e0f2;
    --accent-gold: #e8b923;
    --purple: #46308a;
    --rule: #b9b3d6;
    --panel: #e3e3e3;
    --text: #2b2b2b;
    --muted: #555;
    --white: #ffffff;
  }
  * { box-sizing: border-box; margin: 0; padding: 0; }
  html, body { width: 1200px; height: 2271px; overflow: hidden; background: var(--white); }
  body { font-family: "Open Sans", Arial, sans-serif; color: var(--text); position: relative; }

  .hero { position: absolute; left: 0; top: 0; width: 1200px; height: 745px; overflow: hidden; background: var(--hero-deep); }
  .hero-art { position: absolute; inset: 0;
    background:
      radial-gradient(circle at 200px 470px, rgba(205,200,225,.85) 0, rgba(160,150,195,.75) 260px, rgba(110,85,140,.6) 420px, rgba(35,16,70,0) 520px),
      linear-gradient(90deg, #4e3a78 0%, #2c1552 70%, var(--hero-deep) 100%); }
  .hero-word { position: absolute; left: 88px; top: 95px; font-weight: 700; font-size: 330px; line-height: 1;
    letter-spacing: 58px; color: rgba(255,255,255,.22); }
  .back { position: absolute; left: 114px; top: 20px; }
  .back-rule { position: absolute; left: 209px; top: 0; width: 1px; height: 65px; background: rgba(255,255,255,.35); }
  .rating { position: absolute; left: 892px; top: 22px; width: 308px; }
  .rating-value { padding-left: 36px; font-size: 33px; font-weight: 600; color: var(--ink-light); line-height: 1.2; }
  .rating-rule { height: 1px; background: rgba(255,255,255,.5); margin-top: 10px; }
  .rating-stars { display: flex; gap: 10px; padding: 12px 0 0 34px; }
  .book-title { position: absolute; left: 168px; top: 395px; display: flex; align-items: center; gap: 20px; }
  .book-title h1 { font-size: 50px; font-weight: 600; color: var(--ink-soft); }
  .book-author { position: absolute; left: 245px; top: 470px; font-size: 30px; font-weight: 400; color: var(--ink-soft); }

  .actions { position: absolute; left: 0; top: 626px; width: 1200px; height: 119px; display: flex;
    border-top: 1px solid rgba(255,255,255,.25);
    background: linear-gradient(180deg, rgba(35,16,70,.35), rgba(35,16,70,.85)); }
  .action { display: flex; align-items: center; justify-content: center; gap: 24px; color: var(--ink-light);
    font-size: 24px; font-weight: 600; letter-spacing: .5px; }
  .action-share { width: 225px; border-right: 1px solid rgba(255,255,255,.25); }
  .action-read { width: 512px; }
  .action-add { width: 463px; background: rgba(120,105,160,.55); }

  .chapter { position: absolute; left: 0; top: 745px; width: 1200px; height: 978px; background: var(--panel);
    border-bottom: 2px solid #c9c9c9; }
  .chapter h2 { position: absolute; left: 70px; top: 68px; font-size: 33px; font-weight: 700; color: var(--purple); }
  .chapter-body { position: absolute; left: 70px; top: 148px; width: 1070px; font-size: 26.5px; font-weight: 300; line-height: 42.5px; color: var(--text); }
  .chapter-body p + p { margin-top: 16px; }
  .sections { position: absolute; left: 104px; top: 529px; width: 989px; list-style: none; }
  .sections li { height: 91px; border-bottom: 2px solid var(--rule); display: flex; align-items: center;
    justify-content: space-between; padding-right: 20px; font-size: 28px; font-weight: 600; color: var(--purple); }

  .similar { position: absolute; left: 68px; top: 1760px; }
  .similar h3 { font-size: 37px; font-weight: 400; color: #4b4560; }
  .shelf { position: absolute; left: 68px; top: 1850px; display: flex; gap: 25px; }
  .book { width: 247px; }
  .cover { width: 247px; height: 271px; }
  .cover-1 { background: linear-gradient(160deg, #2f8a7a, #1c5a50 60%, #3b6f62); }
  .cover-2 { background: linear-gradient(170deg, #2b3e48, #3f5766 55%, #1d2a33); }
  .cover-3 { background: linear-gradient(170deg, #27b3d0, #1394b4 60%, #0f7e9c); }
  .cover-4 { background: linear-gradient(170deg, #5e8ac2, #2d4f86 55%, #0e1f3d); }
  .book-name { margin-top: 16px; padding-left: 4px; font-size: 21.5px; font-weight: 700; color: #333; }
  .book-by { margin-top: 4px; padding-left: 4px; font-size: 21px; font-weight: 400; color: var(--muted); }
</style>
</head>
<body>
  <header class="hero">
    <div class="hero-art" role="img" aria-label="Blurred photo of a clock face behind a purple tint"></div>
    <div class="hero-word" aria-hidden="true">TIME</div>
    <svg class="back" width="48" height="28" viewBox="0 0 48 28" aria-label="Back">
      <path d="M46 14H3M14 3 3 14l11 11" fill="none" stroke="rgba(255,255,255,.6)" stroke-width="2"/>
    </svg>
    <div class="back-rule"></div>
    <div class="rating">
      <div class="rating-value">4.5</div>
      <div class="rating-rule"></div>
      <div class="rating-stars">
        <svg width="160" height="20" viewBox="0 0 160 20" aria-label="4.5 of 5 stars">
          <g fill="#d8d3e6">
            <path id="star" d="M9 1l2.4 5.2 5.6.6-4.2 3.8 1.2 5.6L9 13.4 4 16.2l1.2-5.6L1 6.8l5.6-.6z"/>
            <use href="#star" x="33"/><use href="#star" x="66"/><use href="#star" x="99"/>
          </g>
          <use href="#star" x="132" fill="#7d6f9e"/>
        </svg>
      </div>
    </div>
    <div class="book-title">
      <svg width="56" height="56" viewBox="0 0 56 56" aria-hidden="true">
        <circle cx="28" cy="28" r="25" fill="none" stroke="var(--accent-gold)" stroke-width="3"/>
        <circle cx="28" cy="28" r="14" fill="none" stroke="var(--accent-gold)" stroke-width="3" opacity=".7"/>
      </svg>
      <h1>Rates Beyond Today</h1>
    </div>
    <p class="book-author">by Marlo Venn</p>

    <nav class="actions">
      <div class="action action-share">
        <svg width="48" height="48" viewBox="0 0 48 48" aria-label="Share">
          <g fill="none" stroke="#fff" stroke-width="2.5">
            <circle cx="36" cy="9" r="6"/><circle cx="11" cy="24" r="6"/><circle cx="36" cy="39" r="6"/>
            <path d="M16.5 21 30.5 12M16.5 27 30.5 36"/>
          </g>
        </svg>
      </div>
      <div class="action action-read">
        <svg width="54" height="40" viewBox="0 0 54 40" aria-hidden="true">
          <path d="M27 8C20 3 10 3 3 5v31c7-2 17-2 24 3 7-5 17-5 24-3V5c-7-2-17-2-24 3zM27 8v31" fill="none" stroke="#fff" stroke-width="2.5" stroke-linejoin="round"/>
        </svg>
        READ BOOK
      </div>
      <div class="action action-add">
        <svg width="26" height="26" viewBox="0 0 26 26" aria-hidden="true">
          <path d="M13 1v24M1 13h24" stroke="#fff" stroke-width="3"/>
        </svg>
        ADD TO MY LIST
      </div>
    </nav>
  </header>

  <main class="chapter">
    <h2>Chapter1</h2>
    <div class="chapter-body">
      <p>There are many variations of passages of Lorem Ipsum available, but the majority have suffered alteration in some form, by injected humour, or randomised words which don't look even slightly believable.</p>
      <p>If you are going to use a passage of Lorem Ipsum, you need to be sure there isn't anything embarrassing hidden in the middle of text. All the Lorem Ipsum generators on the Internet tend to repeat predefined chunks as necessary, making this the first true generator on the Internet.</p>
    </div>
    <ul class="sections">
      <li>Chapter 1.1<svg width="14" height="22" viewBox="0 0 14 22"><path d="M2 2l9 9-9 9" fill="none" stroke="#8a85a6" stroke-width="2"/></svg></li>
      <li>Chapter 1.2<svg width="14" height="22" viewBox="0 0 14 22"><path d="M2 2l9 9-9 9" fill="none" stroke="#8a85a6" stroke-width="2"/></svg></li>
      <li>Chapter 1.3<svg width="14" height="22" viewBox="0 0 14 22"><path d="M2 2l9 9-9 9" fill="none" stroke="#8a85a6" stroke-width="2"/></svg></li>
      <li>Chapter 1.4<svg width="14" height="22" viewBox="0 0 14 22"><path d="M2 2l9 9-9 9" fill="none" stroke="#8a85a6" stroke-width="2"/></svg></li>
    </ul>
  </main>

  <section class="similar"><h3>Similar Books</h3></section>
  <div class="shelf">
    <article class="book">
      <div class="cover cover-1" role="img" aria-label="Book cover in teal tones with a pocket watch"></div>
      <p class="book-name">The Clockmaker's Hour</p>
      <p class="book-by">R.T. Alden</p>
    </article>
    <article class="book">
      <div class="cover cover-2" role="img" aria-label="Book cover in slate tones with a vintage aircraft"></div>
      <p class="book-name">The Clockmaker's Hour</p>
      <p class="book-by">R.T. Alden</p>
    </article>
    <article class="book">
      <div class="cover cover-3" role="img" aria-label="Book cover in bright cyan with silhouettes and clock hands"></div>
      <p class="book-name">The Clockmaker's Hour</p>
      <p class="book-by">R.T. Alden</p>
    </article>
    <article class="book">
      <div class="cover cover-4" role="img" aria-label="Book cover in blue tones with a futuristic dial motif"></div>
      <p class="book-name">The Clockmaker's Hour</p>
      <p class="book-by">R.T. Alden</p>
    </article>
  </div>
</body>
</html>
```